Redesign of an insurance website

Attached is an insurance website that I need to redesign. Currently the website is too dark. I like for example www.brenvalo.com . Could you make the website lighter and change the structure a little so that it is more user friendly?

Industry/Entity Type

Insurance

Number of Pages Required

4 page

```html
<!DOCTYPE html>
<html lang="en">
<head>
<meta charset="utf-8">
<title>Stitova.cz – Insurance</title>
<link href="https://fonts.googleapis.com/css2?family=Raleway:wght@400;500;600;700&family=Roboto+Condensed:wght@400;700&family=Open+Sans:wght@400;600;700&display=swap" rel="stylesheet">
<style>
  :root{
    --blue-top:#1f7ac9;
    --blue-brand:#1a7ae0;
    --blue-deep:#0a5aa3;
    --blue-footer:#2b86d6;
    --blue-bottom:#1461b0;
    --panel:rgba(58,140,214,.82);
    --cream:#fefbf2;
    --band:#eff3f6;
    --ink:#1e1e1e;
    --white:#fff;
    --yellow:#f6be1c;
  }
  *{box-sizing:border-box;margin:0;padding:0}
  html,body{width:1030px;height:1200px;overflow:hidden;background:var(--cream)}
  body{font-family:'Raleway',sans-serif;color:var(--ink);position:relative}
  .abs{position:absolute}

  .top-bar{left:0;top:0;width:1030px;height:24px;background:var(--blue-top);color:var(--white);
    font:600 8.5px 'Open Sans',sans-serif;}
  .top-bar span{position:absolute;top:7px}

  .site-header{left:0;top:24px;width:1030px;height:53px;background:var(--white);border-bottom:1px solid #e6e6e6}
  .logo{left:147px;top:11px;font:700 26px 'Raleway',sans-serif;color:var(--blue-brand);letter-spacing:.3px}
  .main-nav{right:147px;top:20px;display:flex;gap:26px;font:400 12px 'Roboto Condensed',sans-serif;color:#222}

  .hero{left:0;top:77px;width:1030px;height:381px;
    background:linear-gradient(180deg,#d9c98a 0%,#a8ad78 30%,#7d8c62 55%,#9c9a90 78%,#b9b5ad 100%)}
  .hero-glow{left:0;top:77px;width:1030px;height:381px;
    background:radial-gradient(ellipse 320px 220px at 470px 150px,rgba(255,240,190,.7),transparent 70%),
               linear-gradient(90deg,rgba(60,90,40,.45),transparent 30%,transparent 75%,rgba(60,90,40,.45));}

  .register{left:658px;top:100px;width:224px;height:310px;background:var(--panel);color:var(--white)}
  .register h2{position:absolute;left:20px;top:18px;font:400 22px 'Raleway',sans-serif;letter-spacing:.5px;line-height:26px}
  .register label{position:absolute;left:20px;font:500 11px/14px 'Raleway',sans-serif}
  .register .field{position:absolute;left:20px;width:190px;height:21px;background:#f4f6f8;border-radius:4px}
  .register .agree{position:absolute;left:64px;top:211px;font:400 7.5px 'Open Sans',sans-serif;display:flex;align-items:center;gap:6px}
  .register .agree i{width:6px;height:6px;background:var(--white);display:block}
  .register .submit{position:absolute;left:152px;top:244px;width:57px;height:21px;background:var(--white);border-radius:4px;
    color:#16335a;font:700 11px 'Open Sans',sans-serif;text-align:center;line-height:21px}
  .register .have{position:absolute;left:13px;top:288px;font:400 9.5px 'Raleway',sans-serif}

  .categories{left:147px;top:439px;width:735px;height:113px;background:var(--blue-deep);display:flex}
  .category{flex:1;border-left:1px solid rgba(255,255,255,.18);text-align:center;color:var(--white);padding-top:15px}
  .category:first-child{border-left:none}
  .category h3{font:700 12px 'Roboto Condensed',sans-serif;letter-spacing:.6px}
  .category svg{display:block;margin:12px auto 0}

  .why{left:0;top:582px;width:1030px;text-align:center}
  .why h2{font:400 32px 'Raleway',sans-serif;color:#111}
  .why p{width:660px;margin:16px auto 0;font:400 12px/18px 'Raleway',sans-serif;color:#222}

  .promo-band{left:0;top:724px;width:1030px;height:205px;background:var(--band)}
  .promo-photo{left:148px;top:740px;width:255px;height:169px;
    background:radial-gradient(ellipse 110px 60px at 110px 70px,#8d98a4,transparent 75%),linear-gradient(180deg,#dfe5ec,#c9d1d9 70%,#e4e8ec)}
  .promo-title{left:422px;top:762px;font:500 21px 'Raleway',sans-serif;color:#222}
  .promo-text{left:423px;top:795px;width:445px;font:400 9px/13px 'Raleway',sans-serif;color:#222}
  .btn-more{left:778px;top:888px;width:94px;height:21px;background:var(--yellow);border-radius:5px;color:var(--white);
    font:700 10.5px 'Open Sans',sans-serif;text-align:center;line-height:21px}

  .links{top:966px;font-family:'Open Sans',sans-serif}
  .links h4{font:700 10px 'Open Sans',sans-serif;letter-spacing:.5px;color:#111;margin-bottom:8px}
  .links li{list-style:none;font-size:9.5px;line-height:17px;color:#222;letter-spacing:.3px}

  .site-footer{left:0;top:1092px;width:1030px;height:80px;background:var(--blue-footer);color:var(--white)}
  .footer-logo{left:137px;top:27px;font:700 23px 'Raleway',sans-serif;color:var(--white)}
  .newsletter-label{left:313px;top:34px;font:400 15px 'Raleway',sans-serif;letter-spacing:.5px}
  .newsletter-input{left:500px;top:25px;width:292px;height:33px;background:#f2f5f8;border-radius:4px;
    font:italic 400 12.5px 'Open Sans',sans-serif;color:#9aa3ad;padding:9px 12px}
  .social{left:812px;top:32px;display:flex;gap:6px}
  .social i{width:20px;height:20px;border:1.5px solid var(--white);border-radius:50%;display:block}

  .bottom-bar{left:0;top:1172px;width:1030px;height:28px;background:var(--blue-bottom);color:var(--white);
    text-align:center;font:400 12px/28px 'Raleway',sans-serif;letter-spacing:.4px}
</style>
</head>
<body>

<div class="abs top-bar">
  <span style="left:148px">hello@stitova.cz</span>
  <span style="left:270px">(02) 555 0182</span>
  <span style="left:336px">/</span>
  <span style="left:352px">071 555 019</span>
  <span style="left:710px">Access your policy</span>
  <span style="left:806px">Login</span>
  <span style="left:853px">English</span>
</div>

<header class="abs site-header">
  <div class="abs logo">Stitova.cz</div>
  <nav class="abs main-nav"><span>Home</span><span>Insurance</span><span>Advice</span><span>About Us</span><span>Contact</span></nav>
</header>

<div class="abs hero" role="img" aria-label="Photo of a mother and small child walking hand in hand along a sunlit country road lined with trees"></div>
<div class="abs hero-glow"></div>

<form class="abs register">
  <h2>Register</h2>
  <label style="top:57px">First name</label><div class="field" style="top:75px"></div>
  <label style="top:109px">Last name</label><div class="field" style="top:127px"></div>
  <label style="top:162px">E-mail</label><div class="field" style="top:181px"></div>
  <div class="agree"><i></i>I agree with Terms and conditions</div>
  <div class="submit">Submit</div>
  <div class="have">You already have an account? Please <b>login</b></div>
</form>

<section class="abs categories">
  <div class="category"><h3>CAR INSURANCE</h3>
    <svg width="56" height="52" viewBox="0 0 56 52" fill="#fff"><path d="M14 14a14 12 0 0 1 28 0z"/><rect x="27" y="13" width="2" height="8"/><path d="M12 30l4-8h24l4 8h3v12h-3v4h-6v-4H18v4h-6v-4H9V30z"/><rect x="18" y="25" width="20" height="5" fill="#0a5aa3"/><circle cx="16" cy="36" r="2.5" fill="#0a5aa3"/><circle cx="40" cy="36" r="2.5" fill="#0a5aa3"/></svg></div>
  <div class="category"><h3>HEALTH INSURANCE</h3>
    <svg width="56" height="52" viewBox="0 0 56 52" fill="#fff"><path d="M28 48L6 26a12 12 0 0 1 22-14a12 12 0 0 1 22 14z"/><path d="M6 27h14l3-7 4 14 4-10 3 3h16" fill="none" stroke="#0a5aa3" stroke-width="2.5"/></svg></div>
  <div class="category"><h3>HOME INSURANCE</h3>
    <svg width="56" height="52" viewBox="0 0 56 52" fill="#fff"><path d="M30 6l14 12h-4v14H20V18h-4z"/><rect x="27" y="24" width="6" height="8" fill="#0a5aa3"/><path d="M6 38c8 0 14 2 20 3h10c3 0 3 3 0 3H26l12 1 12-8c3-1 4 1 2 3L40 48H16l-10-4z"/></svg></div>
  <div class="category"><h3>LIFE INSURANCE</h3>
    <svg width="56" height="52" viewBox="0 0 56 52" fill="#fff"><path d="M12 14a16 12 0 0 1 32 0z"/><circle cx="28" cy="20" r="3"/><path d="M24 26h8l2 12h-3v10h-6V38h-3z"/><circle cx="17" cy="27" r="2.5"/><rect x="14" y="31" width="6" height="16" rx="2"/><circle cx="39" cy="27" r="2.5"/><rect x="36" y="31" width="6" height="16" rx="2"/></svg></div>
</section>

<section class="abs why">
  <h2>Why choose us ?</h2>
  <p>Iceland subway tile whatever sustainable, kickstarter ethical cornhole jean shorts. Vice kogi consectetur YOLO, fashion axe la croix flexitarian. Ugh est normcore, authentic yr air plant dreamcatcher post-ironic migas VHS butcher fashion axe edison bulb. In everyday carry delectus mlkshk kogi, lo-fi ex bitters fanny pack ethical consectetur messenger bag.</p>
</section>

<div class="abs promo-band"></div>
<div class="abs promo-photo" role="img" aria-label="Photo of stacked coins in front of a blurred silver car"></div>
<h2 class="abs promo-title">Get your car insurance today</h2>
<p class="abs promo-text">Iceland subway tile whatever sustainable, kickstarter ethical cornhole jean shorts. Vice kogi consectetur YOLO, fashion axe la croix flexitarian. Ugh est normcore, authentic yr air plant dreamcatcher post-ironic migas VHS butcher fashion axe edison bulb. In everyday carry delectus mlkshk kogi, lo-fi ex bitters fanny pack ethical consectetur messenger bag. Iceland subway tile whatever sustainable, kickstarter ethical cornhole jean shorts. Vice kogi consectetur YOLO, fashion axe la croix flexitarian. Ugh est normcore, authentic yr air.</p>
<div class="abs btn-more">Click for more</div>

<div class="abs links" style="left:157px"><h4>EXPLORE YOUR GOALS</h4><ul><li>Find your goal</li><li>Life events</li></ul></div>
<div class="abs links" style="left:363px"><h4>LIFE INSURANCE</h4><ul><li>Term life insurance</li><li>Whole life insurance</li><li>Universal life insurance</li><li>Variable life insurance</li></ul></div>
<div class="abs links" style="left:559px"><h4>RETIREMENT</h4><ul><li>Variable Annuities</li><li>Individual retirement</li></ul></div>
<div class="abs links" style="left:756px"><h4>INVESTMENTS</h4><ul><li>Brokerage</li><li>Mutual funds</li></ul></div>

<footer class="abs site-footer">
  <div class="abs footer-logo">Stitova.cz</div>
  <div class="abs newsletter-label">Subscribe for newsletter</div>
  <div class="abs newsletter-input">Enter your e-mail</div>
  <div class="abs social" aria-label="Social links"><i></i><i></i><i></i></div>
</footer>
<div class="abs bottom-bar">Copyright 2017 &nbsp; Stitova.cz</div>

</body>
</html>
```